Tides & Ember novel and CD cover designs
"Make dreams come true" theme
Tides & Ember novel and CD cover designs -
Creative Brief
NOVEL TITLE: Tides & Ember AUTHOR: Lorna Pettigrew Sallow GENRE: women’s fiction LENGTH: 114,000-words THEME: making dreams come true Paranormal element: heroine’s dreams are guiding her (one actually comes true in real life, which makes her see she should listen to her intuitions) SETTING: Half of the story takes place in 1977–78 in Coeur d’Alene, ID, half in 2003 (mostly) in California CHARACTERS: (see list at end) SYNOPSIS: Witnessing a horrific car accident makes award-winning singer Josephine Marlow reevaluate her empty Hollywood lifestyle. Spurred by recurring dreams and near-forgotten longings, she returns to Coeur d’Alene, Idaho, with the hopes of reconnecting with her old love and former singing partner Neil Fenwick. But, he spurns her despite her efforts to reconcile. In the end, she discovers her true passion lies in sharing music and, in her attempt to win back Neil’s love, she is able to reconnect with the innocent enjoyment of music they once enjoyed together. She moves forward to teach and share music, finding true fulfillment — and through that, winds up gaining her lost love after all. COMPACT DISK (CD) COVER TITLE: Tides & Ember SINGER/SONGWRITER: Lorna Pettigrew Sallow GENRE: folk and easy listening LENGTH: 5 original songs inspired by the novel TIDES & EMBER CHARACTERS JOSEPHINE MARLOW (heroine) • Striking/curly light blonde hair/green eyes/slim/5’4” • Practical, almost controlling • Disbelieving of intuitions at first, but comes to believe them • Driven • Talented vocalist • Honest • Loyal • Witty • Smart • In love with Neil NEIL FENWICK (hero) • Handsome/honey brown hair/hazel eyes/slim/5’10” • Talented composer/pianist • Frustrated with home responsibilities forced on him by his parents • Dreamer • Home-body • Loner • Loves kids • Honest • Smart • In love with Josie, childhood friend of both Beth and Gordon GORDON WICK • Gorgeous/blonde/blue eyes/athletic/6’1” • Conniving and manipulative • Resourceful • Jock/Athletic • Smart • Loves action • In love w/ Josie, great friends and eventual husband of Beth BETH HOLLOWAY WICK • Pretty/brunette/brown eyes/lanky/5’7” • Follower at first, but comes into her own as a party planner as an adult • Loves catering and planning parties • Lost (in some ways), often looks for guidance • Smart • Loyal • Resourceful • In love with Neil for many years, marries Gordon, hates Josie until near end of story, former best friend of Miranda MIRANDA COLE PERIWELL • Plain/brunette/brown eyes/plump/5’6” • Insightful • Wise • Generous • Friendly • Funny • Josie’s best friend, in love with Todd TODD PERIWELL • Cute/ginger-haired/hazel eyes/wiry/5’9” • Funny • Friendly • Dorky • From Texas • In love with Miranda, friends with Josie
40-something+ women's fiction readers desiring to fulfill life dreams
NOVEL General design concepts to consider: • Prefer artist w/ book COVER DESIGN EXPERIENCE, as there are certain nuances which entice readers pick a book off a shelf • BOOK SIZE: Octavo, 9”X6” • A MUSIC BOX plays a key role in the story between the hero and heroine • The main image guiding the heroine in her dream is a SHAFT OF LIGHT shining on a lake cabin deck. • The CABIN also is a main theme. The structure overlooks the lake has one door, two porthole-shaped windows, a large deck, and a creek running under the deck. • CONCEPTS I LIKE: – Most of the image in black & white and punching it up w/ one main element in color, but I’m not tied to this idea. It appeals to me because it’s representative of the flashback element in the story. – An image reflected in someone’s eye – Half of a face – A shaft of light shining through a door or window to illuminate a key element (perhaps the music box) COMPACT DISK (CD) General design concepts to consider: • Must be adapted from book cover design • Music files will be MP3 format, but may also be printed on physical CD, so need image that will fit in a CD jewel box, or can be printed on CD sleeve. (4.724 inches square, or 4.974 inches square for "bleeds.")

```html
<!DOCTYPE html>
<html lang="en">
<head>
<meta charset="utf-8">
<title>Tides &amp; Ember — Book Cover</title>
<link rel="stylesheet" href="https://fonts.googleapis.com/css2?family=Cormorant+Garamond:wght@400;500&family=Great+Vibes&family=Open+Sans:wght@700&display=swap">
<style>
  :root {
    --canvas-bg: #e6e6e6;
    --photo-light: #c4c4c4;
    --photo-mid: #8a8a8a;
    --photo-dark: #3a3a3a;
    --photo-deep: #1f1f1f;
    --title-white: #ffffff;
    --accent-red: #e0141e;
    --badge-text: #ffffff;
  }
  * { margin: 0; padding: 0; box-sizing: border-box; }
  html, body {
    width: 1200px;
    height: 929px;
    overflow: hidden;
    background: var(--canvas-bg);
  }
  .cover {
    position: absolute;
    left: 354px;
    top: 35px;
    width: 567px;
    height: 862px;
    overflow: hidden;
    background: linear-gradient(180deg, var(--photo-mid) 0%, #a5a5a5 30%, var(--photo-mid) 60%, var(--photo-dark) 100%);
    box-shadow: 0 10px 22px rgba(0,0,0,0.18);
  }
  .photo-backdrop {
    position: absolute;
    inset: 0;
    background:
      radial-gradient(ellipse 60% 30% at 30% 30%, rgba(230,230,230,0.55), rgba(230,230,230,0) 70%),
      linear-gradient(180deg, rgba(0,0,0,0) 60%, rgba(0,0,0,0.45) 100%);
  }
  .photo-pier {
    position: absolute;
    left: 0;
    top: 370px;
    width: 290px;
    height: 280px;
    background:
      linear-gradient(165deg, rgba(70,70,70,0) 0%, rgba(50,50,50,0.85) 35%, rgba(30,30,30,0.9) 60%, rgba(120,120,120,0.6) 85%, rgba(120,120,120,0) 100%);
    clip-path: polygon(0 8%, 100% 55%, 100% 80%, 0 95%);
  }
  .photo-portrait {
    position: absolute;
    right: 0;
    top: 0;
    width: 250px;
    height: 862px;
    background:
      radial-gradient(ellipse 70% 40% at 75% 45%, rgba(215,205,200,0.95), rgba(160,155,150,0.6) 55%, rgba(120,120,120,0) 90%),
      radial-gradient(ellipse 90% 30% at 40% 15%, rgba(210,210,210,0.8), rgba(210,210,210,0) 80%),
      linear-gradient(90deg, rgba(140,140,140,0) 0%, rgba(170,170,170,0.7) 35%, rgba(190,185,180,0.9) 100%);
  }
  .title-line {
    position: absolute;
    color: var(--title-white);
    font-family: "Cormorant Garamond", Georgia, serif;
    font-weight: 500;
    line-height: 1;
    text-shadow: 0 2px 6px rgba(0,0,0,0.35);
    white-space: nowrap;
  }
  .title-first { left: 150px; top: 120px; font-size: 150px; }
  .title-amp {
    position: absolute;
    left: 222px;
    top: 232px;
    font-family: "Great Vibes", cursive;
    font-size: 170px;
    line-height: 1;
    color: var(--accent-red);
  }
  .title-second { left: 185px; top: 400px; font-size: 150px; }
  .tagline {
    position: absolute;
    left: 110px;
    top: 592px;
    font-family: "Cormorant Garamond", Georgia, serif;
    font-size: 36px;
    color: var(--title-white);
    letter-spacing: 1px;
    white-space: nowrap;
  }
  .author {
    position: absolute;
    left: 96px;
    top: 730px;
    font-family: "Great Vibes", cursive;
    font-size: 34px;
    color: var(--accent-red);
    white-space: nowrap;
  }
  .quote-badge {
    position: absolute;
    left: 443px;
    top: 2px;
    width: 120px;
    height: 120px;
    border-radius: 50%;
    background: var(--accent-red);
    display: flex;
    align-items: center;
    justify-content: center;
    padding: 12px 14px;
    text-align: center;
    font-family: "Open Sans", Arial, sans-serif;
    font-weight: 700;
    font-size: 11.5px;
    line-height: 1.25;
    color: var(--badge-text);
  }
</style>
</head>
<body>
  <main class="cover">
    <div class="photo-backdrop" role="img" aria-label="Black and white misty lake scene"></div>
    <div class="photo-pier" role="img" aria-label="Black and white photograph of a lake cabin deck on wooden pilings"></div>
    <div class="photo-portrait" role="img" aria-label="Half of a blonde woman's face with one blue eye, in black and white"></div>
    <div class="quote-badge">“Nothing you can touch, can show you what is really there.”</div>
    <h1>
      <span class="title-line title-first">Tides</span>
      <span class="title-amp">&amp;</span>
      <span class="title-line title-second">Ember</span>
    </h1>
    <p class="tagline">Make dreams come true</p>
    <p class="author">Lorna Pettigrew Sallow</p>
  </main>
</body>
</html>
```